BBQ Catering & Pop-up Restaurant

I'm a catering company and a pop-up restaurant and need a website that will have the following at minimum (I'm open to suggestions): about me section, menu section, events section, a pre-order page. Here is an example of a site that I really like ... https://hollowpitsmoke.example/ . I want to have a pre-order page where people can place orders online and the ability to take credit card payments. I've included a word doc with a draft write up to get started.
Updates

Project Deadline Extended
Reason: I am awaiting feedback from my partner and will be in touch ASAP.

Target Market(s)

BBQ Lovers

Industry/Entity Type

Caterer

Font styles to use
Serif
Other font styles liked:
• we can use multiple fonts where appropriate. I also like a faded, woody type font - which reminds me of the old western movies

Colors

Designer to choose colors to be used in the design.

Requirements
Must have
• I want
• - a smokey, woody, bbq type feel to the site.
• - my logo to be utilized
• - colors I like should compliment the colors in my logo
• - link to sign up for a news letter/ mailing list and something on the back end to capture data
Nice to have
• NA
Should not have
• NA

```html
<!DOCTYPE html>
<html lang="en">
<head>
<meta charset="utf-8">
<title>Ember Row Smoke House BBQ</title>
<link href="https://fonts.googleapis.com/css2?family=Ranchers&family=Raleway:wght@400;500;600&family=Open+Sans:wght@600;700&display=swap" rel="stylesheet">
<style>
:root{
  --paper:#ebebea;
  --paper-dark:#dcdcdb;
  --ink:#1f1f1f;
  --ink-soft:#555;
  --brand-red:#8c1c1c;
  --accent:#f5a800;
  --wood:#3a2a20;
  --wood-dark:#2a1d15;
  --white:#fff;
  --title-grey:#6d6d6d;
}
*{box-sizing:border-box;margin:0;padding:0}
html,body{width:1200px;height:2862px;overflow:hidden}
body{background:var(--paper);font-family:"Raleway",sans-serif;color:var(--ink);position:relative}
.display{font-family:"Ranchers",cursive;letter-spacing:1px}
.label{font-family:"Open Sans",sans-serif;font-weight:700}
section,header,footer{position:absolute;left:0;width:1200px}

/* header */
.site-header{top:0;height:118px;background:linear-gradient(#f2f2f1,var(--paper))}
.brand{position:absolute;left:75px;top:40px;display:flex;align-items:center;gap:10px}
.brand-dot{width:30px;height:30px;border-radius:50%;background:var(--brand-red)}
.brand-name{font-family:"Ranchers",cursive;font-size:22px;color:var(--brand-red)}
.main-nav{position:absolute;right:75px;top:50px;display:flex;gap:42px}
.main-nav a{font-family:"Open Sans",sans-serif;font-weight:700;font-size:13px;color:var(--ink);text-decoration:none;text-transform:uppercase;letter-spacing:.5px}
.main-nav a.current{color:var(--brand-red)}

/* hero */
.hero{top:118px;height:452px;background:radial-gradient(ellipse at 60% 40%,#7a4a2c 0%,#4a2c1c 45%,#2a1a12 100%)}
.hero-title{position:absolute;top:170px;width:100%;text-align:center;color:var(--white);font-size:47px;line-height:52px;text-transform:uppercase}
.hero-dots{position:absolute;top:403px;left:0;width:100%;display:flex;justify-content:center;gap:6px}
.hero-dots span{width:12px;height:12px;border-radius:50%;background:var(--white)}
.hero-dots span:first-child{background:var(--accent)}

/* welcome */
.welcome{top:570px;height:355px;text-align:center}
.welcome h1{margin-top:42px;font-size:29px;font-weight:400;text-transform:uppercase}
.welcome p{margin:22px auto 0;width:1080px;font-size:15px;line-height:29px;color:var(--ink-soft)}
.btn-outline{display:inline-block;border:2px solid var(--brand-red);color:var(--brand-red);font-family:"Open Sans",sans-serif;font-weight:700;font-size:14px;text-transform:uppercase;padding:0;height:50px;line-height:46px;text-decoration:none;background:transparent}
.welcome .btn-outline{margin-top:27px;width:180px}

/* menu */
.menu{top:925px;height:453px;background:repeating-linear-gradient(90deg,var(--wood) 0 120px,var(--wood-dark) 120px 123px,#3f2e23 123px 240px,var(--wood-dark) 240px 243px)}
.menu-card{position:absolute;left:75px;top:45px;width:1050px;height:363px;background:var(--white);text-align:center}
.menu-card h2{margin-top:35px;font-size:27px;font-weight:400;text-transform:uppercase}
.menu-items{position:absolute;top:92px;left:17px;display:flex;gap:40px}
.menu-item{width:313px}
.menu-photo{height:164px}
.menu-item h3{margin-top:18px;font-size:17px;color:#333}
.menu-item .price{font-size:17px;color:var(--brand-red)}

/* events */
.events{top:1378px;height:630px;text-align:center}
.events h2{margin-top:50px;font-size:29px;font-weight:400;text-transform:uppercase}
.event-list{position:absolute;top:114px;left:75px;display:flex;gap:30px}
.event-card{width:330px;height:366px;background:var(--white);text-align:left}
.event-photo{height:216px}
.event-date{margin:28px 0 0 23px;font-size:14px;color:var(--brand-red);text-transform:uppercase}
.event-title{margin:2px 0 0 23px;font-size:30px;line-height:34px;color:var(--title-grey);font-weight:400;text-transform:uppercase}
.events .btn-outline{position:absolute;top:530px;left:496px;width:208px}

/* info */
.info{top:2008px;height:332px;background:linear-gradient(100deg,#2c2620 0%,#4a3a2c 40%,#3c3026 70%,#6a5a3a 100%)}
.info-box{position:absolute;top:47px;height:237px;border:1px solid rgba(255,255,255,.45);background:rgba(0,0,0,.35);text-align:center;color:var(--white)}
.info-box.hours{left:78px;width:507px}
.info-box.location{left:615px;width:510px}
.info-box svg{margin-top:22px}
.info-box h3{font-size:25px;font-weight:400;text-transform:uppercase;margin-top:10px}
.info-box p{font-size:14px;line-height:18px;margin-top:8px}
.info-box p.strong{margin-top:16px}
.info-box .highlight{color:var(--accent)}

/* newsletter */
.newsletter{top:2340px;height:330px;background:repeating-linear-gradient(90deg,var(--wood) 0 130px,var(--wood-dark) 130px 133px,#3f2e23 133px 260px,var(--wood-dark) 260px 263px);text-align:center;color:var(--white)}
.newsletter h2{margin-top:78px;font-size:27px;font-weight:400;text-transform:uppercase}
.newsletter p{margin-top:22px;font-size:15px;color:#e3dcd6}
.signup{position:absolute;top:193px;left:317px;display:flex;gap:10px}
.signup .field{width:423px;height:50px;background:var(--white);color:#777;font-size:14px;line-height:50px;text-align:left;padding-left:15px}
.signup .submit{width:135px;height:50px;background:var(--accent);color:var(--white);font-size:15px;line-height:50px;text-transform:uppercase}

/* footer */
.site-footer{top:2670px;height:192px;background:var(--paper)}
.footer-nav{position:absolute;left:75px;top:44px;display:flex;gap:30px}
.footer-nav a{font-family:"Open Sans",sans-serif;font-weight:700;font-size:11px;color:var(--ink);text-decoration:none;text-transform:uppercase}
.footer-brand{position:absolute;left:75px;top:102px;display:flex;align-items:center;gap:8px}
.footer-brand .brand-dot{width:24px;height:24px}
.footer-brand .brand-name{font-size:18px}
.copyright{position:absolute;left:215px;top:102px;font-size:11px;line-height:18px;color:#333}
.follow{position:absolute;left:898px;top:68px;font-size:12px;color:var(--brand-red);text-transform:uppercase}
.social{position:absolute;left:898px;top:98px;display:flex;gap:24px}
.social span{width:24px;height:24px;border-radius:50%;background:#8a8a8a}
</style>
</head>
<body>

<header class="site-header">
  <div class="brand"><span class="brand-dot"></span><span class="brand-name">Ember Row</span></div>
  <nav class="main-nav">
    <a class="current" href="#">Home</a><a href="#">About me</a><a href="#">Menu</a><a href="#">Events</a><a href="#">Preorder</a><a href="#">Contact us</a>
  </nav>
</header>

<section class="hero" role="img" aria-label="Meats and bread grilling over a barbecue pit">
  <h1 class="hero-title display">We are in catering company and<br>pop-up restaurant</h1>
  <div class="hero-dots"><span></span><span></span><span></span><span></span></div>
</section>

<section class="welcome">
  <h1 class="display">Welcome to Ember Row Smoke House BBQ</h1>
  <p>Aliquam molestie, mi et imperdiet euismod, dui purus auctor tellus, et interdum lacus lectus et ante. Sed accumsan sollicitudin sapien, sit amet adipiscing turpis gravida ac. In congue, neque ac lobortis volutpat, libero mauris varius mi, vitae suscipit ipsum ligula vitae risus. Duis aliquam nibh a dui iaculis viverra id a velit. Vivamus egestas risus in magna varius commodo. Sed semper viverra egestas. Etiam pretium porttitor lectus, vel ornare neque porta volutpat.</p>
  <a class="btn-outline" href="#">Read more</a>
</section>

<section class="menu">
  <div class="menu-card">
    <h2 class="display">Our Menu</h2>
    <div class="menu-items">
      <div class="menu-item">
        <div class="menu-photo" role="img" aria-label="Glazed beef short ribs on a plate" style="background:linear-gradient(135deg,#d49a2a,#5a2a14 55%,#f0e8dc)"></div>
        <h3 class="label">Beef Short Ribs</h3><div class="price label">$20/lb</div>
      </div>
      <div class="menu-item">
        <div class="menu-photo" role="img" aria-label="Sauced beef back ribs" style="background:linear-gradient(135deg,#3a2418,#6e3a1e 50%,#2a1a12)"></div>
        <h3 class="label">Beef Back Ribs</h3><div class="price label">$18/lb</div>
      </div>
      <div class="menu-item">
        <div class="menu-photo" role="img" aria-label="Sliced smoked beef brisket" style="background:linear-gradient(135deg,#2a1a14,#7a3a26 50%,#3a1f16)"></div>
        <h3 class="label">Beef Brisket</h3><div class="price label">$22/lb</div>
      </div>
    </div>
  </div>
</section>

<section class="events">
  <h2 class="display">Events</h2>
  <div class="event-list">
    <article class="event-card">
      <div class="event-photo" role="img" aria-label="Crowd lined up outside a brick building" style="background:linear-gradient(#b0c4d8,#c4a880 45%,#6a6a6a)"></div>
      <div class="event-date label">Jul 30, 2017</div>
      <h3 class="event-title display">Vestibulum ante ipsum primis</h3>
    </article>
    <article class="event-card">
      <div class="event-photo" role="img" aria-label="Friends gathered around an outdoor grill" style="background:linear-gradient(135deg,#e8d8a0,#5a7a3a 50%,#3a4a2a)"></div>
      <div class="event-date label">Jul 30, 2017</div>
      <h3 class="event-title display">Vestibulum ante ipsum primis</h3>
    </article>
    <article class="event-card">
      <div class="event-photo" role="img" aria-label="Guests served from a catering buffet" style="background:linear-gradient(135deg,#2a3040,#8a8a80 50%,#d0d4d8)"></div>
      <div class="event-date label">Jul 30, 2017</div>
      <h3 class="event-title display">Vestibulum ante ipsum primis</h3>
    </article>
  </div>
  <a class="btn-outline" href="#">View all events</a>
</section>

<section class="info" role="img" aria-label="Blurred barbecue grill backdrop">
  <div class="info-box hours">
    <svg width="46" height="46" viewBox="0 0 46 46"><circle cx="23" cy="23" r="20" fill="none" stroke="#fff" stroke-width="4"/><path d="M23 12v12h-8" fill="none" stroke="#fff" stroke-width="4"/></svg>
    <h3 class="display">Our Hours</h3>
    <p class="label">Open for Lunch 6 days a week</p>
    <p class="label strong">Mon. Closed!</p>
    <p class="label highlight">Tue.–Sun. 11–Sold Out! 2 or 3pm</p>
  </div>
  <div class="info-box location">
    <svg width="46" height="46" viewBox="0 0 46 46"><path d="M23 2c-8.5 0-15 6.5-15 15 0 11 15 27 15 27s15-16 15-27c0-8.5-6.5-15-15-15z" fill="#fff"/><circle cx="23" cy="17" r="6" fill="#3a3028"/></svg>
    <h3 class="display">Our Location</h3>
    <p class="label">On Austin's historic East Side</p>
    <p class="label strong">412 Kiln Street, Austin, TX 78702</p>
    <p class="label highlight">Get Directions</p>
  </div>
</section>

<section class="newsletter">
  <h2 class="display">Newsletter Signup</h2>
  <p>Aliquam molestie, mi et imperdiet euismod, dui purus auctor tellus, et interdum lacus lectus et ante.</p>
  <div class="signup">
    <div class="field">Enter Email Address</div>
    <div class="submit label">Sign up</div>
  </div>
</section>

<footer class="site-footer">
  <nav class="footer-nav">
    <a href="#">Home</a><a href="#">About me</a><a href="#">Menu</a><a href="#">Events</a><a href="#">Preorder</a><a href="#">Contact us</a>
  </nav>
  <div class="footer-brand"><span class="brand-dot"></span></div>
  <p class="copyright">Copyright © 2017, Ember Row.<br>All Right Reserved</p>
  <div class="follow label">Follow us</div>
  <div class="social"><span></span><span></span><span></span><span></span><span></span></div>
</footer>

</body>
</html>
```